The Brightwater Compass Business Card

We need an attractive business card with the logo that we bought from ArtVantly last year.
Our mission is to contribute to change the way today's leaders manage business companies bringing value to the workplace and helping them to build a new model of creating wealth.
Our logo is clear about our values : we seek Positive Change through People and are convinced that the pursuit of individual well-being and the chase of economic results can converge with the right management.
Management Consulting
Corinne Fabrelle
+34 612 98 70 31
corinne.fabrelle@thebrightwatercompass-mail.net
www.thebrightwatercompass-mail.net

```html
<!DOCTYPE html>
<html lang="en">
<head>
<meta charset="utf-8">
<title>The Brightwater Compass – Business Card</title>
<link href="https://fonts.googleapis.com/css2?family=Marcellus+SC&family=Open+Sans:wght@400&display=swap" rel="stylesheet">
<style>
  :root {
    --teal: #0f8380;
    --shadow-grey: #b4b4b4;
    --ink: #444444;
    --paper: #ffffff;
    --backdrop: #ececec;
  }
  * { margin: 0; padding: 0; box-sizing: border-box; }
  html, body { width: 1200px; height: 987px; overflow: hidden; background: var(--backdrop); }
  .canvas { position: relative; width: 1200px; height: 987px; }
  .card {
    position: absolute; left: 293px; width: 615px; height: 350px;
    background: var(--paper); border-radius: 22px; overflow: hidden;
    box-shadow: 0 3px 10px rgba(0,0,0,0.18);
  }
  .card--front { top: 131px; }
  .card--back { top: 506px; }
  .card__wave { position: absolute; inset: 0; }
  .brand {
    position: absolute; text-align: center;
    font-family: "Marcellus SC", serif; font-weight: 400; white-space: nowrap;
  }
  .brand__dot { display: block; margin: 0 auto 12px; border-radius: 50%; }
  .card--front .brand { left: 275px; width: 330px; top: 38px; color: var(--paper); font-size: 25px; }
  .card--front .brand__dot { width: 58px; height: 58px; background: var(--paper); }
  .card--back .brand { left: 0; width: 615px; top: 96px; color: var(--teal); font-size: 32px; }
  .card--back .brand__dot { width: 80px; height: 80px; background: var(--teal); margin-bottom: 16px; }
  .holder {
    position: absolute; left: 33px; top: 212px;
    font-family: "Marcellus SC", serif; font-size: 25px; color: var(--teal); letter-spacing: 0.5px;
  }
  .contacts { position: absolute; left: 33px; top: 258px; list-style: none;
    font-family: "Open Sans", sans-serif; font-size: 15px; color: var(--ink); }
  .contacts li { display: flex; align-items: center; height: 23.5px; }
  .contacts svg { width: 14px; height: 14px; margin-right: 9px; fill: var(--teal); flex: none; }
</style>
</head>
<body>
<main class="canvas">
  <section class="card card--front">
    <svg class="card__wave" viewBox="0 0 615 350" aria-hidden="true">
      <path fill="var(--shadow-grey)" d="M0,24 C40,168 150,212 300,212 C430,212 560,218 615,350 L615,0 L0,0 Z"/>
      <path fill="var(--teal)" d="M0,0 H615 V345 C560,200 430,192 300,192 C150,192 40,150 0,10 Z"/>
    </svg>
    <div class="brand"><span class="brand__dot"></span>The Brightwater Compass</div>
    <h1 class="holder">Corinne Fabrelle</h1>
    <ul class="contacts">
      <li><svg viewBox="0 0 16 16"><path d="M3.5 1.5l2.5 0 1 3.5-1.6 1.2a8 8 0 0 0 4.4 4.4L11 9l3.5 1v2.5c0 1-1 2-2 2A11 11 0 0 1 1.5 3.5c0-1 1-2 2-2z"/></svg>+34 612 98 70 31</li>
      <li><svg viewBox="0 0 16 16"><path d="M1 3h14v1.2L8 8.6 1 4.2z"/><path d="M1 5.8l7 4.4 7-4.4V13H1z"/></svg>corinne.fabrelle@thebrightwatercompass-mail.net</li>
      <li><svg viewBox="0 0 16 16"><circle cx="8" cy="8" r="7"/><path fill="#fff" d="M5 4.5c1.5-.5 2.5.5 2 1.8S5 7 5.5 9s2 1 1.5 3c-1.5-.3-3.5-2-3.7-4S4 5 5 4.5zM10 3.8c1.5.7 2.7 2.2 2.7 4-1 .3-1.8-.5-2.2-1.5s.2-1.7-.5-2.5z"/></svg>www.thebrightwatercompass-mail.net</li>
    </ul>
  </section>
  <section class="card card--back">
    <div class="brand"><span class="brand__dot"></span>The Brightwater Compass</div>
  </section>
</main>
</body>
</html>
```